Payroll Brochure

Create a brochure with the copy i have provided . A simple easy tp read brochure that shows wat we do we handle payroll taxes insurance 401k etc

```html
<!DOCTYPE html>
<html lang="en">
<head>
<meta charset="UTF-8">
<title>Payroll Services Brochure</title>
<link rel="stylesheet" href="https://fonts.googleapis.com/css2?family=Montserrat:wght@400;700&display=swap">
<style>
  :root {
    --gold: #e2c462;
    --red: #c8191f;
    --white: #ffffff;
    --photo-dark: #6b5a4e;
  }
  * { margin: 0; padding: 0; box-sizing: border-box; }
  html, body { width: 848px; height: 1200px; overflow: hidden; }
  body { font-family: 'Montserrat', sans-serif; background: var(--red); }
  .brochure { position: relative; width: 848px; height: 1200px; background: var(--red); }
  .sidebar { position: absolute; left: 0; top: 0; width: 294px; height: 1200px; background: var(--gold); }
  .service-photo { position: absolute; left: 0; width: 294px; height: 118px; }
  .service-name {
    position: absolute; left: 61px; color: var(--red);
    font-weight: 700; font-size: 24px; line-height: 30px; letter-spacing: 0.2px;
  }
  .features { position: absolute; left: 351px; width: 450px; }
  .feature { margin-bottom: 16px; }
  .feature:last-child { margin-bottom: 0; }
  .feature h3 {
    color: var(--gold); font-weight: 700; font-size: 12.8px;
    letter-spacing: 0.6px; line-height: 16px; text-transform: uppercase;
  }
  .feature p { color: var(--white); font-size: 13px; line-height: 16.2px; letter-spacing: 0.3px; }
  .divider { position: absolute; left: 351px; width: 440px; height: 1px; background: var(--gold); }
</style>
</head>
<body>
<div class="brochure">
  <aside class="sidebar">
    <svg class="service-photo" style="top:119px" role="img" aria-label="Photo of white puzzle pieces with person icons, a hand placing a red piece" viewBox="0 0 294 118" preserveAspectRatio="none">
      <defs><linearGradient id="g1" x1="0" x2="1"><stop offset="0" stop-color="#e6e6e6"/><stop offset="0.45" stop-color="#d8d8d8"/><stop offset="0.6" stop-color="#7a4a36"/><stop offset="1" stop-color="#a0705a"/></linearGradient></defs>
      <rect width="294" height="118" fill="url(#g1)"/>
    </svg>
    <h2 class="service-name" style="top:246px">On Boarding</h2>

    <svg class="service-photo" style="top:385px" role="img" aria-label="Photo of a hand circling blue people icons on a screen" viewBox="0 0 294 118" preserveAspectRatio="none">
      <defs><linearGradient id="g2" x1="0" x2="1"><stop offset="0" stop-color="#8fb3d0"/><stop offset="0.5" stop-color="#c7dbe9"/><stop offset="1" stop-color="#e3edf4"/></linearGradient></defs>
      <rect width="294" height="118" fill="url(#g2)"/>
    </svg>
    <h2 class="service-name" style="top:512px">Applicant<br>Tracking</h2>

    <svg class="service-photo" style="top:688px" role="img" aria-label="Photo of workers wearing orange hard hats" viewBox="0 0 294 118" preserveAspectRatio="none">
      <defs><linearGradient id="g3" x1="0" y1="0" x2="0" y2="1"><stop offset="0" stop-color="#d9dde2"/><stop offset="0.45" stop-color="#d8562a"/><stop offset="1" stop-color="#6d5446"/></linearGradient></defs>
      <rect width="294" height="118" fill="url(#g3)"/>
    </svg>
    <h2 class="service-name" style="top:813px">Time and<br>Attendance</h2>

    <svg class="service-photo" style="top:942px" role="img" aria-label="Photo of a businessman touching a compliance word cloud with laws, rules, standards and security" viewBox="0 0 294 118" preserveAspectRatio="none">
      <defs><linearGradient id="g4" x1="0" x2="1"><stop offset="0" stop-color="#3a3c3f"/><stop offset="0.5" stop-color="#7d7f82"/><stop offset="1" stop-color="#3a3c3f"/></linearGradient></defs>
      <rect width="294" height="118" fill="url(#g4)"/>
    </svg>
    <h2 class="service-name" style="top:1068px">ACA<br>Compliance</h2>
  </aside>

  <section class="features" style="top:117px">
    <div class="feature"><h3>Customize your on boarding</h3>
      <p>you can customize your on boarding experience to your&nbsp; hiring needs as well as provide multiple workflows for different employee types.&nbsp; The on boarding experience can be branded for you, providing a personalized experience for the employees.</p></div>
    <div class="feature"><h3>Custom document management</h3>
      <p>Our custom document mapping feature lets you use your own forms and documents as part of the on boarding and hiring process.&nbsp; When these forms are completed – and electronically signed – they stay in history as long as needed.</p></div>
    <div class="feature"><h3>Intuitive</h3>
      <p>with a focus on the user experience, your employees will find it easy and quick to get on boarded with you.</p></div>
  </section>
  <div class="divider" style="top:385px"></div>

  <section class="features" style="top:410px">
    <div class="feature"><h3>Create and post jobs</h3>
      <p>you can create jobs with just a few clicks and post them on all the popular job sites.</p></div>
    <div class="feature"><h3>Hire the right people</h3>
      <p>by posting on popular job boards, as well as a proprietary database of job seekers, you will reach more candidates.&nbsp; You can choose to receive profiles of candidates that only match your background and specifications.</p></div>
    <div class="feature"><h3>Manage the hiring process</h3>
      <p>review candidates via video or online conferencing, review voice interviews, schedule in person interviews, have candidates answer certain online questions, and manage this entire process to find the right people.&nbsp; Once hired, they can be on boarded automatically.</p></div>
  </section>
  <div class="divider" style="top:691px"></div>

  <section class="features" style="top:718px">
    <div class="feature"><h3>Make time entry easy</h3>
      <p>Simplify time tracking so you can spend less time on payroll tasks.</p></div>
    <div class="feature"><h3>Everywhere access</h3>
      <p>Web interface, mobile apps, and on-premise time clocks allow employees to log their time wherever they are.</p></div>
    <div class="feature"><h3>Plug and play time clocks</h3>
      <p>Time clocks are delivered ready-to-use with little or no setup required.</p></div>
  </section>
  <div class="divider" style="top:921px"></div>

  <section class="features" style="top:945px">
    <div class="feature"><h3>Client tools</h3>
      <p>provide you with reporting and analysis tools online so you can monitor ACA information and be proactive in managing your needs.</p></div>
    <div class="feature"><h3>Affordability test</h3>
      <p>provide your with information about plan affordability with their employees so they can stay in compliance.</p></div>
    <div class="feature"><h3>Large employer analysis</h3>
      <p>analyze your&nbsp; control groups to determine if you will fall under the rules of ACA for large employer groups.</p></div>
  </section>
</div>
</body>
</html>
```